Sherwood Ads

Would like to have new web ads announcing opening of a new pediatric office (Brightfern Pediatrics - Sherwood). First and only dedicated pediatric clinic in Sherwood. Ads need to be following sizes: 160x160, 180x180, 300x250, 336x280, 728x90, 920x250, 1080x1080, 1200x627. Sample of previous ad attached.

```html
<!DOCTYPE html>
<html lang="en">
<head>
<meta charset="utf-8">
<title>Brightfern Pediatrics – Now Open in Sherwood</title>
<link rel="stylesheet" href="https://fonts.googleapis.com/css2?family=Fredoka:wght@500;600;700&family=Nunito:wght@600;700;800&family=Pacifico&display=swap">
<style>
  :root{
    --purple:#6a4fb6;
    --purple-light:#8f7ad6;
    --purple-pale:#cfc6ee;
    --blue:#2f4fa6;
    --red:#ef3a2c;
    --yellow:#f5c12f;
    --gold:#e0a815;
    --ink:#3a3a48;
    --white:#ffffff;
  }
  *{margin:0;padding:0;box-sizing:border-box}
  html,body{width:1200px;height:627px;overflow:hidden;background:var(--white)}
  .ad{position:relative;width:1200px;height:627px;overflow:hidden;background:var(--white);font-family:"Nunito",sans-serif;color:var(--ink)}
  .photo{position:absolute;left:540px;top:0;width:660px;height:570px;
    background:radial-gradient(ellipse at 60% 45%,#f3d9cc 0%,#e9d6cf 30%,#d9d4cf 55%,#c9cbc4 100%)}
  .shapes{position:absolute;inset:0}
  .content{position:absolute;inset:0;z-index:2}

  .brand{position:absolute;left:62px;top:22px;display:flex;align-items:center;gap:60px}
  .brand-dot{width:110px;height:110px;border-radius:50%;background:var(--purple)}
  .brand-name{font-family:"Fredoka",sans-serif;font-weight:600;font-size:46px;line-height:1;color:var(--purple)}

  .headline{position:absolute;left:30px;top:155px;width:510px;text-align:center;font-family:"Fredoka",sans-serif}
  .kicker{font-size:36px;line-height:40px;font-weight:600;color:var(--purple);letter-spacing:1px;display:flex;justify-content:center;align-items:center;gap:14px}
  .spark{width:30px;height:24px}
  .first-only{font-size:74px;font-weight:700;line-height:76px;margin-top:4px;letter-spacing:1px;white-space:nowrap}
  .first-only .first{color:var(--blue)}
  .first-only .amp{color:var(--purple)}
  .first-only .only{color:var(--red)}
  .subline{font-size:27px;line-height:30px;font-weight:500;color:var(--ink);margin-top:2px;letter-spacing:.5px;white-space:nowrap}

  .open-banner{position:absolute;left:92px;top:322px;width:420px;height:38px;background:var(--purple);
    clip-path:polygon(0 0,100% 0,97% 100%,0 100%);display:flex;align-items:center;padding-left:32px;
    font-family:"Fredoka",sans-serif;font-weight:600;font-size:25px;color:var(--white);white-space:nowrap}
  .open-banner .now{color:var(--yellow);margin-right:8px}
  .pin-badge{position:absolute;left:42px;top:314px;width:56px;height:56px;border-radius:50%;background:var(--white);
    border:3px solid var(--purple);display:flex;align-items:center;justify-content:center}

  .care{position:absolute;left:68px;top:374px;width:440px;font-size:19.5px;font-weight:700;line-height:1.25;color:var(--ink)}
  .care .hl{color:var(--blue)}
  .care .indent{padding-left:122px;display:block}

  .features{position:absolute;left:40px;top:442px;display:flex}
  .feature{text-align:center;font-size:11.5px;font-weight:800;line-height:1.35;border-right:2px dashed var(--purple-pale);white-space:nowrap}
  .feature.patients{width:112px}
  .feature.sick{width:125px}
  .feature.checkups{width:125px}
  .feature.experts{width:150px;border-right:none}
  .feature svg{width:52px;height:52px;margin:0 auto 8px;display:block}
  .feature .top{color:var(--ink);display:block}
  .feature .bottom{display:block}
  .c-purple{color:var(--purple)} .c-yellow{color:var(--gold)}

  .address{position:absolute;left:42px;top:594px;display:flex;align-items:center;gap:10px;font-size:11.5px;font-weight:700;color:var(--white);letter-spacing:.3px;white-space:nowrap}
  .cta{position:absolute;left:736px;top:566px;width:436px;height:44px;border-radius:22px;background:var(--white);
    display:flex;align-items:center;gap:14px;padding-left:18px;font-family:"Fredoka",sans-serif;font-weight:600;font-size:20px;color:var(--purple);white-space:nowrap}
  .cta .hl{color:var(--red)}

  .seal{position:absolute;left:1012px;top:2px;width:176px;height:176px;border-radius:50%;background:var(--purple);
    border:5px solid var(--white);box-shadow:0 0 0 2px var(--purple-light);color:var(--white);
    display:flex;flex-direction:column;align-items:center;padding-top:18px;text-align:center}
  .seal .tag{font-size:12.5px;font-weight:700;line-height:1.3;margin-top:6px}
  .seal .script{font-family:"Pacifico",cursive;font-size:20px;line-height:1.25;margin-top:4px}
  .seal .script .gold{color:var(--yellow)}
  .seal .heart-bottom{margin-top:4px}
</style>
</head>
<body>
<div class="ad">
  <div class="photo" role="img" aria-label="Photo of a smiling pediatrician listening to a toddler's heartbeat with a stethoscope while the mother and older sister with a plush toy watch"></div>

  <svg class="shapes" width="1200" height="627" viewBox="0 0 1200 627" aria-hidden="true">
    <path d="M0 0 L614 0 C575 150 525 360 548 580 L0 580 Z" fill="var(--white)"/>
    <path d="M614 0 C575 150 525 360 548 580" fill="none" stroke="var(--purple)" stroke-width="16"/>
    <path d="M900 560 C1000 520 1100 470 1200 420 L1200 627 L900 627 Z" fill="var(--purple-light)"/>
    <path d="M0 548 C250 572 480 540 700 562 C880 580 1040 530 1200 478 L1200 627 L0 627 Z" fill="var(--purple)"/>
    <path d="M660 605 C690 590 700 610 730 596" fill="none" stroke="var(--white)" stroke-width="1.5" stroke-dasharray="4 4"/>
    <g stroke="var(--yellow)" stroke-width="3" stroke-linecap="round">
      <line x1="1152" y1="545" x2="1158" y2="533"/><line x1="1166" y1="552" x2="1178" y2="544"/><line x1="1170" y1="564" x2="1184" y2="562"/>
    </g>
    <g stroke="var(--purple-pale)" stroke-width="3" stroke-linecap="round">
      <line x1="478" y1="28" x2="478" y2="44"/><line x1="470" y1="36" x2="486" y2="36"/>
      <line x1="517" y1="82" x2="517" y2="98"/><line x1="509" y1="90" x2="525" y2="90"/>
    </g>
  </svg>

  <div class="content">
    <div class="brand">
      <div class="brand-dot"></div>
      <div class="brand-name">Brightfern<br>Pediatrics</div>
    </div>

    <div class="headline">
      <div class="kicker">
        <svg class="spark" viewBox="0 0 30 24"><g stroke="var(--red)" stroke-width="3" stroke-linecap="round"><line x1="4" y1="4" x2="14" y2="9"/><line x1="2" y1="13" x2="14" y2="13"/><line x1="4" y1="21" x2="14" y2="17"/></g></svg>
        SHERWOOD’S
        <svg class="spark" viewBox="0 0 30 24"><g stroke="var(--red)" stroke-width="3" stroke-linecap="round"><line x1="26" y1="4" x2="16" y2="9"/><line x1="28" y1="13" x2="16" y2="13"/><line x1="26" y1="21" x2="16" y2="17"/></g></svg>
      </div>
      <div class="first-only"><span class="first">FIRST</span> <span class="amp">&amp;</span> <span class="only">ONLY</span></div>
      <div class="subline">DEDICATED PEDIATRIC CLINIC</div>
    </div>

    <div class="open-banner"><span class="now">NOW OPEN</span> IN SHERWOOD!</div>
    <div class="pin-badge">
      <svg width="26" height="30" viewBox="0 0 26 30"><path d="M13 28 C5 18 3 14 3 10 A10 10 0 0 1 23 10 C23 14 21 18 13 28Z" fill="none" stroke="var(--purple)" stroke-width="2.5"/><circle cx="13" cy="10" r="3.5" fill="none" stroke="var(--purple)" stroke-width="2.5"/></svg>
    </div>

    <p class="care">
      <svg width="22" height="18" viewBox="0 0 22 18" style="vertical-align:-2px;margin-right:6px"><path d="M11 17 C3 11 1 8 1 5 A4.5 4.5 0 0 1 11 3 A4.5 4.5 0 0 1 21 5 C21 8 19 11 11 17Z" fill="var(--yellow)"/></svg>Compassionate care for <span class="hl">newborns,</span>
      <span class="indent"><span class="hl">children &amp; teens.</span></span>
    </p>

    <div class="features">
      <div class="feature patients">
        <svg viewBox="0 0 52 52" fill="none" stroke="var(--purple)" stroke-width="2.5"><circle cx="20" cy="14" r="8"/><path d="M4 44 C4 32 11 26 20 26 C29 26 36 32 36 44 Z"/><circle cx="37" cy="22" r="6"/><path d="M34 32 C42 31 48 36 48 44 L38 44"/></svg>
        <span class="top">ACCEPTING</span><span class="bottom c-purple">NEW PATIENTS</span>
      </div>
      <div class="feature sick">
        <svg viewBox="0 0 52 52" fill="none" stroke="var(--purple)" stroke-width="2.5"><rect x="5" y="9" width="42" height="36" rx="4"/><line x1="5" y1="18" x2="47" y2="18"/><line x1="15" y1="5" x2="15" y2="13"/><line x1="37" y1="5" x2="37" y2="13"/><circle cx="17" cy="30" r="6"/><line x1="17" y1="27" x2="17" y2="33"/><line x1="14" y1="30" x2="20" y2="30"/><g stroke-width="2"><rect x="28" y="24" width="5" height="5"/><rect x="36" y="24" width="5" height="5"/><rect x="28" y="33" width="5" height="5"/><rect x="36" y="33" width="5" height="5"/></g></svg>
        <span class="top">SAME-DAY</span><span class="bottom c-purple">SICK VISITS</span>
      </div>
      <div class="feature checkups">
        <svg viewBox="0 0 52 52" fill="none" stroke="var(--gold)" stroke-width="2.5"><circle cx="24" cy="16" r="10"/><path d="M8 46 C8 34 15 29 24 29 C33 29 40 34 40 46 Z"/><path d="M36 34 L46 30 L46 40 C46 44 42 46 41 46"/><polyline points="38,38 41,41 45,35"/></svg>
        <span class="top">WELL-CHILD</span><span class="bottom c-yellow">CHECKUPS</span>
      </div>
      <div class="feature experts">
        <svg viewBox="0 0 52 52" fill="none" stroke="var(--purple)" stroke-width="2.5"><circle cx="22" cy="15" r="9"/><path d="M6 46 C6 34 13 28 22 28 C31 28 38 34 38 46 Z"/><path d="M38 26 L47 29 L47 37 C47 42 42 45 38 46 C34 45 29 42 29 37 L29 29 Z"/><line x1="38" y1="32" x2="38" y2="40"/><line x1="34" y1="36" x2="42" y2="36"/></svg>
        <span class="top">EXPERIENCED</span><span class="bottom c-purple">PEDIATRIC EXPERTS</span>
      </div>
    </div>

    <div class="address">
      <svg width="18" height="22" viewBox="0 0 26 30"><path d="M13 28 C5 18 3 14 3 10 A10 10 0 0 1 23 10 C23 14 21 18 13 28Z" fill="none" stroke="var(--white)" stroke-width="2.5"/><circle cx="13" cy="10" r="3.5" fill="none" stroke="var(--white)" stroke-width="2.5"/></svg>
      4870 SW MEADOWLARK WAY STE B-210, SHERWOOD, OR 97140, UNITED STATES
    </div>

    <div class="cta">
      <svg width="36" height="32" viewBox="0 0 36 32" fill="none" stroke="var(--purple)" stroke-width="2.2"><rect x="2" y="4" width="32" height="26" rx="3"/><line x1="2" y1="11" x2="34" y2="11"/><line x1="10" y1="1" x2="10" y2="7"/><line x1="26" y1="1" x2="26" y2="7"/><circle cx="11" cy="20" r="4"/><g stroke-width="1.6"><rect x="19" y="15" width="4" height="4"/><rect x="26" y="15" width="4" height="4"/><rect x="19" y="22" width="4" height="4"/><rect x="26" y="22" width="4" height="4"/></g></svg>
      <span>SCHEDULE YOUR <span class="hl">FIRST VISIT</span> TODAY!</span>
    </div>

    <div class="seal">
      <svg width="18" height="15" viewBox="0 0 22 18"><path d="M11 17 C3 11 1 8 1 5 A4.5 4.5 0 0 1 11 3 A4.5 4.5 0 0 1 21 5 C21 8 19 11 11 17Z" fill="var(--yellow)"/></svg>
      <p class="tag">Healthy Kids.<br>Happier Futures.</p>
      <p class="script">Right Here in<br><span class="gold">Sherwood!</span></p>
      <svg class="heart-bottom" width="14" height="12" viewBox="0 0 22 18"><path d="M11 17 C3 11 1 8 1 5 A4.5 4.5 0 0 1 11 3 A4.5 4.5 0 0 1 21 5 C21 8 19 11 11 17Z" fill="var(--purple-pale)"/></svg>
    </div>
  </div>
</div>
</body>
</html>
```